Design a styled business card for an intimacy and attachment psychologist

I am a Psychologist providing online therapy to patients across the United States. My work is interpersonal and emotion-focused, with an emphasis on the client-therapist relationship. My primary areas of work are very personal, including sexuality and gender, abuse and trauma, and grief and loss. My target audience will be adults of all ages 18+.
My business card should convey a warm and inviting feeling of professionalism that is also casual and comfortable.
The front should be fairly simple and professional, consisting of:
- My name, Dr. Rosalind Petrakis
- My title, Licensed Psycholigist
- My logo
On either the front or the back, my contact information should be listed:
- ros@drrospetrakis.example
- 555.014.7788
- drrospetrakis.example
On the rear, I would like a description of the areas that I specialize in. This can be formatted in any way that appears stylistically interesting.
Individual and Couples
Relationships and Infidelity
Sexual Health & Aging
Gender Identity & Sexual Orientation
Abuse and Trauma
Sexual Compulsivity & Addiction
Sexual Dysfunction
Target Market(s)
My target audience will be adults of all ages 18+.
Industry/Entity Type
Psychology
Contact Information for Business Card
The front should be fairly simple and professional, consisting of: - My name, Dr. Rosalind Petrakis - My title, Licensed Psycholigist - My logo On either the front or the back, my contact information should be listed: - ros@drrospetrakis.example - 555.014.7788 - drrospetrakis.example On the rear, I would like a description of the areas that I specialize in. This can be formatted in any way that appears stylistically interesting. Individual and Couples Relationships and Infidelity Sexual Health & Aging Gender Identity & Sexual Orientation Abuse and Trauma Sexual Compulsivity & Addiction Sexual Dysfunction
- Follow brand guide

```html
<!DOCTYPE html>
<html lang="en">
<head>
<meta charset="utf-8">
<title>Dr. Rosalind Petrakis — Business Card</title>
<link href="https://fonts.googleapis.com/css2?family=Marcellus&family=Tenor+Sans&display=swap" rel="stylesheet">
<style>
  :root {
    --bg: #2b2b2d;
    --card: #ffffff;
    --navy: #2a2552;
    --purple: #8d43ab;
    --teal: #4bb897;
    --rule-pink: #f1c9c6;
    --ghost: #ececef;
    --ink-soft: #3b3a4a;
  }
  * { box-sizing: border-box; margin: 0; padding: 0; }
  html, body { width: 1200px; height: 900px; overflow: hidden; }
  body {
    background: var(--bg);
    font-family: "Tenor Sans", "Optima", sans-serif;
    color: var(--navy);
    position: relative;
  }
  .card {
    position: absolute;
    left: 250px;
    width: 700px;
    height: 400px;
    background: linear-gradient(135deg, #f7f7f8 0%, var(--card) 55%, #f4f4f6 100%);
    border-radius: 44px;
    overflow: hidden;
  }
  .card--specialties { top: 40px; }
  .card--contact { top: 470px; }

  .ghost-ring {
    position: absolute;
    border: 12px solid var(--ghost);
    border-radius: 50%;
  }
  .card--specialties .ghost-ring { width: 300px; height: 300px; left: 40px; top: 80px; }
  .card--contact .ghost-ring { width: 300px; height: 300px; right: 70px; top: 20px; }

  .brand {
    position: absolute;
    display: flex;
    align-items: center;
    gap: 18px;
  }
  .brand__dot {
    width: 74px; height: 74px;
    border-radius: 50%;
    background: var(--teal);
    flex: none;
  }
  .brand__name {
    font-family: "Marcellus", "Optima", serif;
    color: var(--navy);
    font-size: 38px;
    line-height: 1.05;
    letter-spacing: 1px;
    text-transform: uppercase;
  }
  .brand__name span { display: block; }
  .brand__name .brand__title { font-size: 22px; }
  .card--specialties .brand { left: 300px; top: 42px; }
  .card--contact .brand { left: 70px; top: 120px; }

  .specialties {
    position: absolute;
    right: 50px;
    top: 150px;
    width: 540px;
    text-align: right;
  }
  .specialties__heading {
    font-family: "Marcellus", serif;
    color: var(--purple);
    font-size: 22px;
    letter-spacing: 1px;
    text-transform: uppercase;
    margin-bottom: 14px;
  }
  .specialties__list {
    list-style: none;
    font-size: 17.5px;
    line-height: 1.65;
    color: var(--navy);
  }
  .sep { color: var(--navy); padding: 0 4px; }

  .identity {
    position: absolute;
    left: 70px;
    top: 282px;
    font-size: 19px;
    color: var(--navy);
  }
  .identity__name {
    font-family: "Marcellus", serif;
    text-transform: uppercase;
    letter-spacing: 1px;
  }
  .identity__role { color: var(--ink-soft); }
  .contact-rule {
    position: absolute;
    left: 70px; right: 60px;
    top: 322px;
    height: 1px;
    background: var(--rule-pink);
  }
  .contact {
    position: absolute;
    left: 70px;
    top: 338px;
    font-size: 16.5px;
    color: var(--ink-soft);
    letter-spacing: 0.3px;
  }
  .contact__label, .contact__sep { color: var(--teal); }
  .contact__sep { padding: 0 6px; }
</style>
</head>
<body>

  <section class="card card--specialties">
    <div class="ghost-ring" aria-hidden="true"></div>
    <div class="brand">
      <div class="brand__dot" aria-hidden="true"></div>
      <div class="brand__name">
        <span class="brand__title">Dr.</span>
        <span>Rosalind</span>
        <span>Petrakis</span>
      </div>
    </div>
    <div class="specialties">
      <h2 class="specialties__heading">Specialize In</h2>
      <ul class="specialties__list">
        <li>Stylistically Interesting<span class="sep">|</span>Individual And Couples</li>
        <li>Relationships And Infidelity<span class="sep">|</span>Sexual Health &amp; Aging</li>
        <li>Gender Identity &amp; Sexual Orientation<span class="sep">|</span>Abuse And Trauma</li>
        <li>Sexual Compulsivity &amp; Addiction<span class="sep">|</span>Sexual Dysfunction</li>
      </ul>
    </div>
  </section>

  <section class="card card--contact">
    <div class="ghost-ring" aria-hidden="true"></div>
    <div class="brand">
      <div class="brand__dot" aria-hidden="true"></div>
      <div class="brand__name">
        <span class="brand__title">Dr.</span>
        <span>Rosalind</span>
        <span>Petrakis</span>
      </div>
    </div>
    <p class="identity">
      <span class="identity__name">Dr. Rosalind Petrakis</span>
      <span class="sep">|</span>
      <span class="identity__role">Licensed Psycholigist</span>
    </p>
    <div class="contact-rule" aria-hidden="true"></div>
    <p class="contact">
      <span class="contact__label">T.</span> 555.014.7788
      <span class="contact__sep">|</span><span class="contact__label">E.</span> ros@drrospetrakis.example
      <span class="contact__sep">|</span>www.drrospetrakis.example
    </p>
  </section>

</body>
</html>
```